Relaxation CD Cover

The relaxation cd is unique in that it does not include the typical windchimes, waterfalls, harps, etc. The feel is a mixture of jazz, spanish guitar, spiritual vibes and even some djembe drums. It includes mindfulness techniques that are used in yoga, meditation, and relaxation settings. The title right now is Gentle, Flowing Stillness. The cover should convey calm and cool with a bohemian and somewhat sultry feel. Maybe a bit afrocentric but not too much. A mock-up is attached, which includes a pic of the doctor who created the CD but the pic might be too sexy for the professional role. The color scheme especially the blue in the necklace is part of the branding so necessary to carry out. CD front and back should be consistent. Polish, modern, and clean can coexist with bohemian and relaxed. If you can do this then you've got the job! Please see both pics attached. The headshot is the desired pic to be included if artist does decide to use it but please do not feel limited to using the pics.
Updates

The pic does not have to be used in the pic...less literal please.

Target Market(s)

This CD will not only be marketed via Disc Sprout and Tunevale but also wellness stores, doc's offices;yoga retreats; local afrocentric fairs

Industry/Entity Type

Doctor

Requirements
Must have
• The color of the necklace or emphasize the necklace
Welcoming and relaxed feel (must be clear that this is a relaxation CD)
front and back must be consistent
A clear area where song titles will be located
Nice to have
• If the pic is included it should relate to the overall feel or color scheme...
Should not have
• -Bohemian does not mean messy or overly themed, e.g., too spanish or afrocentric

```html
<!DOCTYPE html>
<html lang="en">
<head>
<meta charset="utf-8">
<title>Gentle, Flowing Stillness — Album Cover</title>
<link href="https://fonts.googleapis.com/css2?family=Raleway:wght@200;300&display=swap" rel="stylesheet">
<style>
  :root {
    --backdrop: #f1f1f1;
    --night-violet: #2c2350;
    --dusk-indigo: #3b3468;
    --olive-glow: #8a8a3a;
    --golden-skin: #b59a3c;
    --sunset-orange: #e0652a;
    --necklace-green: #2fae63;
    --text-light: rgba(255, 255, 255, 0.92);
    --title-mist: rgba(255, 255, 255, 0.55);
    --subtitle-gold: #f3e79a;
  }

  * { margin: 0; padding: 0; box-sizing: border-box; }

  html, body {
    width: 1200px;
    height: 1013px;
    overflow: hidden;
    background: var(--backdrop);
  }

  .stage {
    position: relative;
    width: 1200px;
    height: 1013px;
    display: flex;
    align-items: center;
    justify-content: center;
  }

  .album-cover {
    position: relative;
    width: 940px;
    height: 940px;
    overflow: hidden;
    font-family: "Raleway", "Helvetica Neue", Arial, sans-serif;
  }

  .cover-artwork {
    position: absolute;
    inset: 0;
    width: 100%;
    height: 100%;
  }

  .artist-name {
    position: absolute;
    top: 100px;
    left: 0;
    right: 0;
    text-align: center;
    font-weight: 300;
    font-size: 42px;
    letter-spacing: 3px;
    color: var(--text-light);
    text-transform: uppercase;
  }

  .album-title {
    position: absolute;
    top: 148px;
    left: 0;
    right: 0;
    text-align: center;
    font-weight: 200;
    font-size: 196px;
    line-height: 1;
    letter-spacing: 6px;
    color: var(--title-mist);
    text-transform: uppercase;
  }

  .album-subtitle {
    position: absolute;
    top: 842px;
    left: 0;
    right: 0;
    text-align: center;
    font-weight: 300;
    font-size: 26px;
    letter-spacing: 1px;
    color: var(--subtitle-gold);
    text-transform: uppercase;
  }
</style>
</head>
<body>
  <main class="stage">
    <section class="album-cover">
      <svg class="cover-artwork" viewBox="0 0 940 940" preserveAspectRatio="none"
           role="img" aria-label="Portrait of the artist with beaded green necklace and earrings, framed by line-drawn flowers and leaves in violet, olive and gold tones">
        <defs>
          <linearGradient id="cover-sky" x1="0" y1="0" x2="0" y2="1">
            <stop offset="0" stop-color="var(--night-violet)"/>
            <stop offset="0.35" stop-color="var(--dusk-indigo)"/>
            <stop offset="0.6" stop-color="var(--olive-glow)"/>
            <stop offset="1" stop-color="var(--golden-skin)"/>
          </linearGradient>
          <radialGradient id="cover-warmth" cx="0.12" cy="0.95" r="0.45">
            <stop offset="0" stop-color="var(--sunset-orange)" stop-opacity="0.9"/>
            <stop offset="1" stop-color="var(--sunset-orange)" stop-opacity="0"/>
          </radialGradient>
          <radialGradient id="cover-necklace" cx="0.55" cy="1" r="0.4">
            <stop offset="0" stop-color="var(--necklace-green)" stop-opacity="0.85"/>
            <stop offset="1" stop-color="var(--necklace-green)" stop-opacity="0"/>
          </radialGradient>
        </defs>
        <rect width="940" height="940" fill="url(#cover-sky)"/>
        <rect width="940" height="940" fill="url(#cover-warmth)"/>
        <rect width="940" height="940" fill="url(#cover-necklace)"/>
      </svg>

      <p class="artist-name">Dr. Lorna Vance</p>
      <h1 class="album-title">Gentle</h1>
      <p class="album-subtitle">Flowing Stillness</p>
    </section>
  </main>
</body>
</html>
```